Cocktail Lounge Holiday Coffee Specialties

Irish Coffee $14
Pellow Irish Whiskey, Dorrin's, Fresh Whipped Cream
Cocktail Lounge Coffee $14
Brandy, Vostra, Dorin's, Fresh Whipped Cream
Orange Blossom $12
Belle Ravine Sable Fine Liquor, Fresh Whipped Cream
HBRG Italian Coffee $12
Pontarello Liquor with Fresh Whipped Cream
The Jamaican $12
Lua Soleda with Fresh Whipped Cream

Target Market(s)

Formal Cocktail Lounge crowd 50 years old and above

Requirements
Must have
• Harbor Ridge Rowing Guild logo at top
Nice to have
• will fit in table tent that has corner holders

```html
<!DOCTYPE html>
<html lang="en">
<head>
<meta charset="utf-8">
<title>Cocktail Lounge Holiday Coffee Specialties</title>
<link rel="stylesheet" href="https://fonts.googleapis.com/css2?family=Great+Vibes&family=Cinzel:wght@700&family=Alegreya+Sans:wght@400;700&display=swap">
<style>
  :root {
    --backdrop: #e4e4e4;
    --wood-dark: #4a3526;
    --wood-mid: #6e5140;
    --wood-light: #8a6a55;
    --paper-light: #f7efd6;
    --paper-edge: #e3d2a6;
    --red: #b0262f;
    --green: #1d7a45;
    --ink: #5a4433;
    --garland-green: #1f4a2c;
    --garland-red: #9c2a22;
  }
  html, body {
    margin: 0;
    width: 1200px;
    height: 1200px;
    overflow: hidden;
    background: var(--backdrop);
  }
  .menu-board {
    position: absolute;
    left: 218px;
    top: 40px;
    width: 764px;
    height: 1120px;
    box-shadow: 0 6px 18px rgba(0,0,0,.35);
  }
  .wood-frame {
    position: absolute;
    inset: 0;
    background: linear-gradient(90deg, var(--wood-dark), var(--wood-mid) 30%, var(--wood-light) 55%, var(--wood-mid) 80%, var(--wood-dark));
  }
  .paper {
    position: absolute;
    left: 64px;
    right: 51px;
    top: 8px;
    bottom: 60px;
    background: radial-gradient(ellipse at 50% 40%, var(--paper-light) 40%, var(--paper-edge) 100%);
    text-align: center;
    color: var(--ink);
    font-family: "Alegreya Sans", sans-serif;
  }
  .club-mark {
    position: absolute;
    left: 0;
    right: 0;
    top: 110px;
    display: flex;
    justify-content: center;
    align-items: center;
    gap: 10px;
    font-size: 24px;
    font-weight: 700;
    color: var(--red);
  }
  .club-mark .dot {
    width: 18px;
    height: 18px;
    border-radius: 50%;
    background: var(--red);
  }
  .title-script {
    position: absolute;
    left: 0; right: 0;
    top: 252px;
    margin: 0;
    font-family: "Great Vibes", cursive;
    font-weight: 400;
    font-size: 84px;
    line-height: 1;
    color: var(--green);
  }
  .title-holiday {
    position: absolute;
    left: 0; right: 0;
    top: 318px;
    font-family: "Cinzel", serif;
    font-weight: 700;
    font-size: 62px;
    line-height: 1;
    letter-spacing: 2px;
    color: var(--red);
  }
  .title-sub {
    position: absolute;
    left: 0; right: 0;
    top: 388px;
    font-family: "Cinzel", serif;
    font-weight: 700;
    font-size: 25px;
    letter-spacing: 1px;
    color: var(--green);
  }
  .title-rule {
    position: absolute;
    left: 57px;
    width: 510px;
    top: 422px;
    height: 2px;
    background: var(--green);
  }
  .drink {
    position: absolute;
    left: 0; right: 0;
  }
  .drink-name {
    margin: 0;
    font-size: 31px;
    font-weight: 700;
    line-height: 38px;
    color: var(--red);
  }
  .drink-recipe {
    margin: 0;
    font-size: 25px;
    line-height: 31px;
  }
  .garland {
    position: absolute;
    left: 0;
    right: 0;
    bottom: 0;
    height: 110px;
    background: linear-gradient(180deg, var(--garland-green), #173b22 55%, var(--garland-red) 120%);
  }
</style>
</head>
<body>
  <div class="menu-board">
    <div class="wood-frame" role="img" aria-label="Weathered wood plank border"></div>
    <div class="paper">
      <div class="club-mark"><span class="dot"></span>Harbor Ridge Rowing Guild</div>

      <h1 class="title-script">Cocktail Lounge</h1>
      <div class="title-holiday">HOLIDAY</div>
      <div class="title-sub">COFFEE SPECIALTIES</div>
      <div class="title-rule"></div>

      <div class="drink" style="top:440px">
        <p class="drink-name">Irish Coffee $14</p>
        <p class="drink-recipe">Pellow Irish Whiskey, Dorrin's,<br>Fresh Whipped Cream</p>
      </div>
      <div class="drink" style="top:561px">
        <p class="drink-name">Cocktail Lounge Coffee $14</p>
        <p class="drink-recipe">Brandy, Vostra, Dorin's,<br>Fresh Whipped Cream</p>
      </div>
      <div class="drink" style="top:685px">
        <p class="drink-name">Orange Blossom $12</p>
        <p class="drink-recipe">Belle Ravine Sable Fine Liquor,<br>Fresh Whipped Cream</p>
      </div>
      <div class="drink" style="top:810px">
        <p class="drink-name">HBRG Italian Coffee $12</p>
        <p class="drink-recipe">Pontarello Liquor with<br>Fresh Whipped Cream</p>
      </div>
      <div class="drink" style="top:930px">
        <p class="drink-name">The Jamaican $12</p>
        <p class="drink-recipe">Lua Soleda with Fresh Whipped Cream</p>
      </div>
    </div>
    <div class="garland" role="img" aria-label="Holiday garland of pine, holly, red berries and copper ribbon"></div>
  </div>
</body>
</html>
```